New Light Bulb Box Design

Hi,
I'm introducing a new product to the market in November and I need some new packaging made and designed. Attached is the box standard size and measurements to scale.

I'm looking for the following:
- Business details - VELVET HERON (please search for vector of the business name logo)
- Unique box design which will be eye catching, upmarket and look expensive
- Must include the Logo (only the dog not the outer circle).
- Must include a section for viewing the product inside, product window or clear section, please think outside of box and something unique
- think different colours, consider white or coloured box, possibly brown packaging with embossed sections, coloured inside etc
- Must contain some technical details on packaging which are in attachment
- Inspiration is attached.

I will have two different products which will need to utilise the same box design.

Products are bulbs, think neon, no product shots will be provided.

Thanks

```html
<!DOCTYPE html>
<html lang="en">
<head>
<meta charset="utf-8">
<title>Velvet Heron G125 – Decorative LED Box</title>
<link rel="stylesheet" href="https://fonts.googleapis.com/css2?family=Bebas+Neue&family=Quicksand:wght@500;700&display=swap">
<style>
  :root {
    --canvas: #ffffff;
    --box: #1d1d20;
    --box-edge: #26262a;
    --gold: #e6b450;
    --amber: #f6a623;
    --white: #f4f4f2;
    --grey: #9d9ea4;
    --muted: #5b5c62;
    --label-bg: #ffffff;
  }
  * { box-sizing: border-box; margin: 0; padding: 0; }
  html, body { width: 1200px; height: 868px; overflow: hidden; background: var(--canvas); }
  body { font-family: "Quicksand", sans-serif; color: var(--white); }

  .dieline { position: absolute; left: 80px; top: 154px; display: flex; }
  .panel { position: relative; width: 260px; height: 560px; background: var(--box); border-right: 1px solid var(--box-edge); overflow: hidden; }
  .panel--side { background: linear-gradient(180deg, #222226, #19191c); }

  .display { font-family: "Bebas Neue", sans-serif; line-height: .9; }
  .spec-lumen { font-family: "Quicksand", sans-serif; font-weight: 700; color: var(--gold); font-size: 14px; line-height: 18px; letter-spacing: .3px; }
  .spec-watt { font-size: 46px; color: var(--white); }
  .spec-volt { font-size: 60px; color: var(--grey); }

  /* front */
  .brand { position: absolute; left: 20px; top: 56px; font-weight: 700; font-size: 20px; line-height: 1.05; color: var(--white); }
  .model { position: absolute; left: 20px; top: 104px; font-weight: 700; font-size: 26px; color: var(--white); }
  .finish { position: absolute; left: 160px; top: 60px; font-weight: 700; font-size: 26px; color: transparent; -webkit-text-stroke: 1.4px var(--gold); letter-spacing: 1px; }
  .product-window { position: absolute; left: 40px; top: 150px; width: 210px; height: 220px; border-radius: 60px 60px 90px 40px; background: radial-gradient(circle at 40% 40%, #ffd36b 0%, #f5a524 45%, #6b4a22 100%); border: 6px solid var(--white); }
  .front-specs { position: absolute; left: 20px; bottom: 36px; }
  .base-icon { display: block; width: 16px; height: 14px; margin-bottom: 6px; }

  /* side A */
  .range { position: absolute; right: 18px; top: 50px; text-align: right; }
  .range__kicker { font-weight: 700; font-size: 14px; color: var(--gold); letter-spacing: .5px; }
  .range__type { font-family: "Bebas Neue", sans-serif; font-size: 62px; line-height: .85; color: var(--white); }
  .features { position: absolute; right: 18px; top: 180px; display: flex; flex-direction: column; gap: 34px; align-items: center; }
  .feature { display: flex; flex-direction: column; align-items: center; gap: 6px; font-size: 11px; color: var(--grey); font-weight: 500; }
  .feature svg { width: 34px; height: 34px; }

  /* back */
  .back-head { position: absolute; left: 18px; top: 70px; }
  .brand-slot { position: absolute; right: 18px; top: 98px; width: 96px; font-weight: 700; font-size: 17px; line-height: 1.1; color: var(--gold); text-align: right; }
  .copy { position: absolute; left: 18px; right: 18px; top: 220px; font-size: 10.5px; line-height: 1.5; color: var(--white); font-weight: 500; }
  .temp-scale { position: absolute; left: 18px; right: 18px; top: 380px; }
  .temp-scale__marker { font-size: 10px; font-weight: 700; padding-left: 30px; color: var(--white); }
  .temp-scale__bar { height: 34px; margin-top: 3px; background: linear-gradient(90deg, #f7a21c, #ffd98b 40%, #fff6e4 60%, #d7ecfb); }
  .temp-scale__ends { display: flex; justify-content: space-between; font-size: 10px; margin-top: 4px; color: var(--white); }
  .marks { position: absolute; left: 18px; bottom: 44px; display: flex; gap: 8px; }
  .mark { width: 18px; height: 18px; border: 1.5px solid var(--white); border-radius: 50%; }
  .mark--square { border-radius: 2px; }

  /* side B */
  .bulb-art { position: absolute; left: 20px; top: 56px; width: 70px; height: 140px; border-radius: 35px 35px 14px 14px; background: linear-gradient(180deg, rgba(230,180,80,.35), rgba(230,180,80,.12)); }
  .side-specs { position: absolute; right: 18px; top: 56px; text-align: right; }
  .energy { position: absolute; left: 72px; top: 230px; width: 82px; height: 200px; background: var(--label-bg); border: 1px solid #cfd3d8; padding: 5px; color: #1a1a1a; }
  .energy__head { display: flex; gap: 3px; align-items: center; }
  .energy__flag { width: 18px; height: 12px; background: #2a4fa0; }
  .energy__title { font-size: 7px; font-weight: 700; color: #2a4fa0; }
  .energy__sub { font-size: 4.5px; color: #2a4fa0; margin-top: 1px; }
  .energy__bars { margin-top: 8px; display: flex; flex-direction: column; gap: 4px; }
  .energy__bar { height: 11px; font-size: 7px; font-weight: 700; color: #fff; padding-left: 3px; line-height: 11px; clip-path: polygon(0 0, calc(100% - 5px) 0, 100% 50%, calc(100% - 5px) 100%, 0 100%); }
  .energy__foot { margin-top: 10px; display: flex; gap: 6px; align-items: baseline; font-size: 11px; font-weight: 700; }
  .energy__foot small { font-size: 5px; font-weight: 500; }
  .energy__class { position: absolute; right: -34px; top: 43px; width: 28px; height: 14px; background: #111; color: #fff; font-size: 8px; font-weight: 700; line-height: 14px; text-align: center; clip-path: polygon(5px 0, 100% 0, 100% 100%, 5px 100%, 0 50%); }
</style>
</head>
<body>
<main class="dieline">

  <section class="panel panel--front">
    <div class="brand">Velvet<br>Heron</div>
    <div class="model">G125</div>
    <div class="finish">GOLD</div>
    <div class="product-window" role="img" aria-label="Product window showing a glowing amber filament bulb"></div>
    <div class="front-specs">
      <svg class="base-icon" viewBox="0 0 16 14"><rect x="1" y="1" width="14" height="12" rx="2" fill="none" stroke="#e6b450" stroke-width="1.5"/><line x1="1" y1="5" x2="15" y2="5" stroke="#e6b450"/><line x1="1" y1="9" x2="15" y2="9" stroke="#e6b450"/></svg>
      <div class="spec-lumen">E27 | 260 LUMEN</div>
      <div class="display spec-watt">04 WATT</div>
      <div class="display spec-volt">240V</div>
    </div>
  </section>

  <section class="panel panel--side">
    <div class="range">
      <div class="range__kicker">DECORATIVE</div>
      <div class="range__type">LED</div>
    </div>
    <div class="features">
      <div class="feature">
        <svg viewBox="0 0 34 34" fill="none" stroke="#f4f4f2" stroke-width="1.5"><circle cx="14" cy="14" r="9"/><line x1="11" y1="26" x2="17" y2="26"/><circle cx="23" cy="21" r="7" fill="#1f1f22"/><path d="M23 17v4l3 2"/></svg>
        15000h
      </div>
      <div class="feature">
        <svg viewBox="0 0 34 34" fill="none" stroke="#f4f4f2" stroke-width="1.5"><rect x="10" y="3" width="14" height="28" rx="2"/><rect x="14" y="9" width="6" height="9" fill="#f4f4f2"/></svg>
        on/off 10000x
      </div>
      <div class="feature">
        <svg viewBox="0 0 34 34" fill="none" stroke="#f4f4f2" stroke-width="1.5"><circle cx="10" cy="14" r="7"/><line x1="7" y1="24" x2="13" y2="24"/><circle cx="25" cy="14" r="7" stroke="#e6b450"/><line x1="22" y1="24" x2="28" y2="24" stroke="#e6b450"/></svg>
        &lt;1 sec
      </div>
    </div>
  </section>

  <section class="panel panel--back">
    <div class="back-head">
      <div class="spec-lumen">E27 | 260 LUMEN</div>
      <div class="display spec-watt">04 WATT</div>
      <div class="display spec-volt">240V</div>
    </div>
    <div class="brand-slot">Velvet Heron</div>
    <p class="copy">Lorem ipsum dolor sit amet, id persius perfecto est, scripta eruditi in sed, ea pro vocent blandit. Brute dicat habemus et has, mea at velit recusabo. Ius ne nisl suscipit, eos in illud feugiat. Usu ei urbanitas reprimique, ei vel tota mutat, quo atqui virtute gloriatur te. Vis paulo exerci numquam ad.</p>
    <div class="temp-scale">
      <div class="temp-scale__marker">▼ 2700K</div>
      <div class="temp-scale__bar"></div>
      <div class="temp-scale__ends"><span>2000K</span><span>6500K</span></div>
    </div>
    <div class="marks">
      <span class="mark"></span><span class="mark"></span><span class="mark"></span><span class="mark mark--square"></span>
    </div>
  </section>

  <section class="panel panel--side">
    <div class="bulb-art" role="img" aria-label="Line drawing of a classic filament bulb"></div>
    <div class="side-specs">
      <div class="spec-lumen">E27 | 260 LUMEN</div>
      <div class="display spec-watt">04 WATT</div>
      <div class="display spec-volt">240V</div>
    </div>
    <div class="energy">
      <div class="energy__head"><span class="energy__flag"></span><span class="energy__title">ENERG</span></div>
      <div class="energy__sub">енергия · ενεργεια</div>
      <div class="energy__bars">
        <div class="energy__bar" style="width:50%;background:#00a651">A++</div>
        <div class="energy__bar" style="width:58%;background:#50b848">A+</div>
        <div class="energy__bar" style="width:66%;background:#bed630">A</div>
        <div class="energy__bar" style="width:74%;background:#fff200;color:#333">B</div>
        <div class="energy__bar" style="width:82%;background:#fdb913">C</div>
        <div class="energy__bar" style="width:90%;background:#f37021">D</div>
      </div>
      <div class="energy__class">A+</div>
      <div class="energy__foot">4 <small>kWh/1000h</small></div>
    </div>
  </section>

</main>
</body>
</html>
```